Prairie Reading Alliance - Minds Unbound Website

We need a website designed for a PR + Marketing Campaign (Minds Unbound: Our Daily Craft) for the Prairie Reading Alliance (PRA), the largest statewide library association in the country.

The final design should communicate an empowerment to libraries, its innovative practices, and how they are helping and improving the lives of all communities (of all ages, backgrounds, experiences).

The look should be bold, captivating; meanwhile also simple, clean, easy-to-navigate.

LAYOUT (five pages total):
Page 1: Home – Intro
Animated logo transitioning into simple landing page.
Must feature #shelvesinmotion and eventually featuring video.

Page 2: About the Campaign
Graphics/photos optional, text below:
Broad Objectives and Goals
Minds Unbound: Our Daily Craft seeks to broaden the awareness of library services to the public and provide resources to librarians working in the state in order to promote libraries as vital, technology-centered institutions in the community.
The campaign provides a platform for the sharing of ideas and resources that strengthen the image of the library profession and the services provided by libraries in Texas.
Related goals include: providing librarians with the tools necessary to influence key supporters, shifting the perspectives of libraries as a center for books to a center for emerging technology and the cultivation of ideas, and spreading the message of the campaign through both traditional and social media outlets.
Librarians and information professionals are encouraged to actively participate in the campaign through social media outlets, using the hashtag #shelvesinmotion, and by contributing content in the Ideas Shared portion of the campaign website.

Page 3: Toolkit – downloadable items
Downloadable Campaign Materials for library professionals
Buttons leading to subpages or one large page covering the topics below

Page 4: Ideas Shared: What We Do: Interactive element page
Toolkit
Here are the tools and downloadable materials for #shelvesinmotion everywhere. Use these campaign designs to showcase the innovation happening in your library! Check back as we continue to update this page with new content.
Logos
Campaign logos in various formats for use on your own customized designs.
Print Materials
Flyers, bookmarks, posters and more!
Web & Interactive
Graphics for social media and the Web.
Coming soon: #shelvesinmotion campaign video!
PR & Marketing
Sample press releases, emails, and customizable content for a variety of library types: school, academic, public, and special.

Page 5: Contact Us Page
Can either be a sub-section of the About Us page, or a stand-alone link.
Standard submission form with the ability to upload documents for the Ideas Shared section.
Contact Us
Have a question or comment? Want to contribute a summary and photos or video of your innovative programs for the Ideas Shared section? Please get in touch!
NAME:
EMAIL:
PHONE:
ADDRESS: ?
MESSAGE:
ATTACHMENTS (upload)

MUST HAVE:
-Maintain the color-scheme of the logo (attached)
-The WEBSITE design must innovation and excitement. a contemporary design/layout that demonstrates vitality
-Somewhere on every page, we would like an interactive element for viewers, such as a stream from Chatterloop/Peepline with hashtags.
-Countdown to Campaign Launch
-Can we include animation? We are striving to create movement with the abstract icon in our log.

PLEASE AVOID:
-NO pastels, NO soft colors, nothing that might be considered feminine (pinks, etc); we do want to stear away from stereotypes (NO books, NO library buildings, NO reading conceptual designs) and standard icons (NO lightbulbs and NO lightning designs)

AUDIENCE/MARKET:
THE PUBLIC (also includes all kinds of librarians and their supporters: information, reference, school, public, special, law, academic, students, educators, administration, support staff, lay and advocates)

AUDIENCE/MARKET:

Requirements
Must have
• The final design should communicate an empowerment to libraries, its innovative practices, and how they are helping and improving the lives of all communities (of all ages, backgrounds, experiences).
• The look should be bold, captivating; meanwhile also simple, clean, easy-to-navigate.
• LAYOUT (five pages total):
• Page 1: Home – Intro
• Animated logo transitioning into simple landing page.
• Must feature #shelvesinmotion and eventually featuring video.
• Page 2: About the Campaign
• Graphics/photos optional, text below:
• Broad Objectives and Goals
• Minds Unbound: Our Daily Craft seeks to broaden the awareness of library services to the public and provide resources to librarians working in the state in order to promote libraries as vital, technology-centered institutions in the community.
• The campaign provides a platform for the sharing of ideas and resources that strengthen the image of the library profession and the services provided by libraries in Texas.
• Related goals include: providing librarians with the tools necessary to influence key supporters, shifting the perspectives of libraries as a center for books to a center for emerging technology and the cultivation of ideas, and spreading the message of the campaign through both traditional and social media outlets.
• Librarians and information professionals are encouraged to actively participate in the campaign through social media outlets, using the hashtag #shelvesinmotion, and by contributing content in the Ideas Shared portion of the campaign website.
• Page 3: Toolkit – downloadable items
• Downloadable Campaign Materials for library professionals
• Buttons leading to subpages or one large page covering the topics below
• Page 4: Ideas Shared: What We Do: Interactive element page
• Toolkit
• Here are the tools and downloadable materials for #shelvesinmotion everywhere. Use these campaign designs to showcase the innovation happening in your library! Check back as we continue to update this page with new content.
• Logos
• Campaign logos in various formats for use on your own customized designs.
• Print Materials
• Flyers, bookmarks, posters and more!
• Web & Interactive
• Graphics for social media and the Web.
• Coming soon: #shelvesinmotion campaign video!
• PR & Marketing
• Sample press releases, emails, and customizable content for a variety of library types: school, academic, public, and special.
• Page 5: Contact Us Page
• Can either be a sub-section of the About Us page, or a stand-alone link.
• Standard submission form with the ability to upload documents for the Ideas Shared section.
• Contact Us
• Have a question or comment? Want to contribute a summary and photos or video of your innovative programs for the Ideas Shared section? Please get in touch!
• NAME:
• EMAIL:
• PHONE:
• ADDRESS: ?
• MESSAGE:
• ATTACHMENTS (upload)
• MUST HAVE:
• -Maintain the color-scheme of the logo (attached)
• -The WEBSITE design must innovation and excitement. a contemporary design/layout that demonstrates vitality
• -Somewhere on every page, we would like an interactive element for viewers, such as a stream from Chatterloop/Peepline with hashtags.
• -Countdown to Campaign Launch
• -Can we include animation? We are striving to create movement with the abstract icon in our log.
Should not have
• PLEASE AVOID:
• -NO pastels, NO soft colors, nothing that might be considered feminine (pinks, etc); we do want to stear away from stereotypes (NO books, NO library buildings, NO reading conceptual designs) and standard icons (NO lightbulbs and NO lightning designs)

```html
<!DOCTYPE html>
<html lang="en">
<head>
<meta charset="utf-8">
<title>Minds Unbound – Ideas Shared</title>
<link href="https://fonts.googleapis.com/css2?family=Cinzel:wght@400;700&family=Arimo:wght@400&family=Lato:wght@400;700&display=swap" rel="stylesheet">
<style>
:root{
  --blue:#2a9fd8;
  --blue-dark:#1d7fb3;
  --charcoal:#3a3a3a;
  --ink:#2b2b2b;
  --text:#555;
  --muted:#777;
  --card:#f5f5f5;
  --line:#d8d8d8;
  --white:#fff;
}
*{margin:0;padding:0;box-sizing:border-box}
html,body{width:834px;height:1200px;overflow:hidden}
body{position:relative;background:var(--white);font-family:'Lato',sans-serif;color:var(--text)}

/* Header */
.site-header{position:absolute;left:0;top:0;width:834px;height:58px;background:var(--charcoal);z-index:2}
.brand{position:absolute;left:56px;top:0;width:147px;height:118px;background:var(--white);border-radius:0 0 8px 8px;box-shadow:0 3px 8px rgba(0,0,0,.35);z-index:3;display:flex;flex-direction:column;align-items:center;justify-content:center;gap:6px}
.brand-dot{width:34px;height:34px;border-radius:50%;background:var(--blue)}
.brand-name,.brand-tag{font-family:'Cinzel',serif;font-weight:400;color:var(--blue);text-align:center;line-height:1}
.brand-name{font-size:15px}
.brand-tag{font-size:8.5px;letter-spacing:1.5px}
.main-nav{position:absolute;right:60px;top:13px;display:flex;gap:22px;align-items:center}
.main-nav a{font-family:'Cinzel',serif;font-size:13px;color:var(--white);text-decoration:none;padding:6px 8px}
.main-nav a.active{color:var(--blue);border:2px solid var(--blue);border-radius:3px}

/* Hero */
.hero{position:absolute;left:0;top:58px;width:834px;height:417px;background:linear-gradient(90deg,#7a7a7a 0%,#8c8c8c 35%,#5f5f5f 60%,#6f6f6f 100%)}
.hero-video{position:absolute;left:348px;top:42px;width:450px;height:335px;border-radius:14px;background:#1e1e1e}
.hero-video .screen{position:absolute;left:38px;top:30px;width:371px;height:272px;background:linear-gradient(135deg,#d9dde0,#8a8f94 60%,#4a4d52)}
.hero-video .play{position:absolute;left:152px;top:93px}
.hero-title{position:absolute;left:57px;top:134px;max-width:285px;white-space:nowrap;font-family:'Cinzel',serif;font-weight:400;font-size:23px;color:var(--white);letter-spacing:.3px}
.hero-sub{position:absolute;left:57px;top:170px;font-family:'Arimo',sans-serif;font-size:21px;line-height:29px;color:var(--white)}
.btn-primary{position:absolute;left:56px;top:249px;width:118px;height:34px;background:var(--blue);color:var(--white);font-family:'Cinzel',serif;font-size:14px;display:flex;align-items:center;justify-content:center;border-radius:2px;box-shadow:0 2px 0 var(--blue-dark);text-decoration:none}

/* Ideas shared */
.section-title{position:absolute;left:0;top:508px;width:834px;text-align:center;font-family:'Cinzel',serif;font-weight:400;font-size:27px;color:var(--ink)}
.section-title .accent{color:var(--blue)}
.divider{position:absolute;left:130px;top:545px}
.intro-lead{position:absolute;left:60px;top:598px;width:714px;text-align:center;font-family:'Cinzel',serif;font-size:14px;line-height:19px;color:var(--ink)}
.intro-body{position:absolute;left:90px;top:655px;width:654px;text-align:center;font-size:11.5px;line-height:18px;color:#444}

.story{position:absolute;width:350px;height:112px;background:var(--card);border:1px solid var(--line);display:flex}
.story-media{width:123px;height:110px;flex:none}
.story-body{padding:11px 12px 0 15px}
.story-title{font-family:'Cinzel',serif;font-weight:400;font-size:14.5px;color:var(--ink);margin-bottom:6px;white-space:nowrap}
.story-text{font-size:9.6px;line-height:14px;color:var(--muted)}
.story-link{display:inline-block;margin:6px 0 0 3px;font-family:'Cinzel',serif;font-size:10.5px;color:var(--blue)}
.s1{left:56px;top:740px}.s2{left:429px;top:740px}.s3{left:56px;top:878px}.s4{left:429px;top:878px}
.m1{background:linear-gradient(135deg,#0b1a33,#1e5fa8 60%,#6fb8ef)}
.m2{background:linear-gradient(160deg,#0d2b4f,#2a7ac0 55%,#a9d6f2)}
.m3{background:linear-gradient(180deg,#05070c,#16243a 60%,#3a6fa4)}
.m4{background:linear-gradient(135deg,#0e3f73,#2e86c8 55%,#0b2947)}

/* Footer */
.site-footer{position:absolute;left:0;top:1027px;width:834px;height:151px;background:var(--charcoal);box-shadow:inset 0 8px 10px -6px rgba(0,0,0,.5)}
.f-col{position:absolute;top:22px}
.f-col h4{font-size:11.5px;font-weight:700;color:var(--white);padding-bottom:4px;border-bottom:1px solid #5a5a5a;margin-bottom:8px}
.f-links{list-style:none}
.f-links li{font-size:8.5px;color:#e6e6e6;line-height:17.3px}
.f-links li::before{content:'›';margin-right:6px;color:#bbb}
.f-contact{font-size:8.5px;color:#e6e6e6;line-height:12.5px}
.f-contact .row{display:flex;gap:8px;margin-bottom:6px}
.f-contact svg{flex:none;margin-top:1px}
.f-news p{font-size:8.5px;color:#e6e6e6;line-height:12.5px;margin-bottom:6px}
.email-field{width:143px;height:18px;background:var(--white);font-size:7.5px;font-style:italic;color:#888;padding:4px 5px}
.btn-subscribe{display:inline-block;margin-top:8px;background:var(--blue);color:var(--white);font-size:10px;padding:3px 8px}
.f-brand{position:absolute;left:648px;top:26px;width:112px;text-align:center}
.f-brand .name{font-family:'Cinzel',serif;font-size:12px;color:#bbb}
.socials{margin-top:10px;display:grid;grid-template-columns:1fr 1fr;gap:5px 6px;text-align:left}
.social{display:flex;align-items:center;gap:4px;font-size:8px;color:var(--white)}
.social i{width:10px;height:10px;border-radius:50%;background:var(--white);flex:none}
.col-sep{position:absolute;top:30px;width:1px;height:110px;background:#474747}
.legal{position:absolute;left:0;top:1178px;width:834px;height:22px;background:var(--blue);font-size:8.5px;font-weight:700;color:var(--white)}
.legal .copy{position:absolute;left:78px;top:6px}
.legal .policy{position:absolute;right:72px;top:6px}
</style>
</head>
<body>

<header class="site-header">
  <nav class="main-nav">
    <a href="#">Home</a>
    <a href="#">About</a>
    <a href="#">Toolkit</a>
    <a href="#" class="active">Idea Shared</a>
    <a href="#">Contact</a>
  </nav>
</header>
<div class="brand">
  <span class="brand-dot"></span>
  <span class="brand-name">Minds Unbound</span>
  <span class="brand-tag">OUR DAILY CRAFT</span>
</div>

<section class="hero" role="img" aria-label="Hands holding a tablet showing a campaign video of a smiling professional">
  <div class="hero-video">
    <div class="screen" role="img" aria-label="Video still of a presenter in a suit at a desk">
      <svg class="play" width="68" height="68" viewBox="0 0 68 68" aria-hidden="true">
        <circle cx="34" cy="34" r="31" fill="rgba(0,0,0,.15)" stroke="#fff" stroke-width="3"/>
        <path d="M27 20 L50 34 L27 48 Z" fill="#fff"/>
      </svg>
    </div>
  </div>
  <h1 class="hero-title">Libraries Are Essential</h1>
  <p class="hero-sub">To The Creation &amp; Sharing Of<br>Ideas In The Community</p>
  <a class="btn-primary" href="#">Get Started</a>
</section>

<h2 class="section-title"><span class="accent">Ideas</span> Shared</h2>
<svg class="divider" width="574" height="20" viewBox="0 0 574 20" aria-hidden="true">
  <line x1="0" y1="8" x2="260" y2="8" stroke="#ccc" stroke-dasharray="1 1"/>
  <line x1="314" y1="8" x2="574" y2="8" stroke="#ccc" stroke-dasharray="1 1"/>
  <circle cx="287" cy="10" r="8" fill="var(--blue)"/>
</svg>

<p class="intro-lead">Looking For Inspiration From Other #shelvesinmotion? Browse Below To Learn About<br>Creative And Innovative Library Activities That Are Taking Place Around You.</p>
<p class="intro-body">Library professionals are encouraged to share ideas and program success stories! What innovative or non-traditional services do you provide? Do you have photos or videos describing how you power ideas in your institution? If so, visit our Contact Us page to upload content for consideration to be added to this site. Thank you for sharing!</p>

<article class="story s1">
  <div class="story-media m1" role="img" aria-label="Hand touching a glowing digital interface"></div>
  <div class="story-body"><h3 class="story-title">Lorem ipsum dolor sit</h3>
  <p class="story-text">Lorem ipsum dolor sit amet, consectetuer adip iscing elit, sed diam nonummy nibh euismod tincidunt ut laoreet dolore magna aliquam...</p>
  <a class="story-link" href="#">Read Story</a></div>
</article>
<article class="story s2">
  <div class="story-media m2" role="img" aria-label="Blue 3D word cloud about search optimisation"></div>
  <div class="story-body"><h3 class="story-title">Lorem ipsum dolor sit</h3>
  <p class="story-text">Lorem ipsum dolor sit amet, consectetuer adip iscing elit, sed diam nonummy nibh euismod tincidunt ut laoreet dolore magna aliquam...</p>
  <a class="story-link" href="#">Read Story</a></div>
</article>
<article class="story s3">
  <div class="story-media m3" role="img" aria-label="Colourful app icons rising from a tablet"></div>
  <div class="story-body"><h3 class="story-title">Lorem ipsum dolor sit</h3>
  <p class="story-text">Lorem ipsum dolor sit amet, consectetuer adip iscing elit, sed diam nonummy nibh euismod tincidunt ut laoreet dolore magna aliquam...</p>
  <a class="story-link" href="#">Read Story</a></div>
</article>
<article class="story s4">
  <div class="story-media m4" role="img" aria-label="Blue head silhouette surrounded by formulas and sketches"></div>
  <div class="story-body"><h3 class="story-title">Lorem ipsum dolor sit</h3>
  <p class="story-text">Lorem ipsum dolor sit amet, consectetuer adip iscing elit, sed diam nonummy nibh euismod tincidunt ut laoreet dolore magna aliquam...</p>
  <a class="story-link" href="#">Read Story</a></div>
</article>

<footer class="site-footer">
  <div class="f-col" style="left:80px;width:82px">
    <h4>Quick Links</h4>
    <ul class="f-links"><li>Home</li><li>About Us</li><li>Toolkit</li><li>Ideas Shared</li><li>Contact</li></ul>
  </div>
  <span class="col-sep" style="left:194px"></span>
  <div class="f-col f-contact" style="left:229px;width:157px">
    <h4>Contact Information</h4>
    <div class="row"><svg width="8" height="11" viewBox="0 0 8 11"><path d="M4 0a4 4 0 0 0-4 4c0 3 4 7 4 7s4-4 4-7a4 4 0 0 0-4-4z" fill="#fff"/><circle cx="4" cy="4" r="1.5" fill="var(--charcoal)"/></svg><span>Lorem ipsum dolor sit consectetuer adipiscing elit, diam nonummy nibh euismod.</span></div>
    <div class="row"><svg width="9" height="9" viewBox="0 0 9 9"><path d="M1 0h2l1 2-1 1a5 5 0 0 0 3 3l1-1 2 1v2a1 1 0 0 1-1 1A8 8 0 0 1 0 1a1 1 0 0 1 1-1z" fill="#fff"/></svg><span style="font-weight:700">(555) 014-2290</span></div>
    <div class="row"><svg width="10" height="8" viewBox="0 0 10 8"><rect x=".5" y=".5" width="9" height="7" fill="none" stroke="#fff"/><path d="M.5 .5 5 4.5 9.5 .5" fill="none" stroke="#fff"/></svg><span>hello@mindsunbound.org</span></div>
  </div>
  <span class="col-sep" style="left:416px"></span>
  <div class="f-col f-news" style="left:451px;width:146px">
    <h4>Newsletter Sign Up</h4>
    <p>Lorem ipsudolor sit coec adipiscin elitsite amet</p>
    <div class="email-field">Email Address</div>
    <span class="btn-subscribe">SUBSCRIBE</span>
  </div>
  <span class="col-sep" style="left:627px"></span>
  <div class="f-brand">
    <div class="name">Minds Unbound</div>
    <div class="socials">
      <span class="social"><i></i>Chatterloop</span>
      <span class="social"><i></i>Peepline</span>
      <span class="social"><i></i>Circlecast</span>
      <span class="social"><i></i>Worknet</span>
    </div>
  </div>
</footer>
<div class="legal">
  <span class="copy">Copyright © 2015 Mindsunbound All Right Reserved</span>
  <span class="policy">Privacy Policy &nbsp;&nbsp;|&nbsp;&nbsp; Terms &amp; Conditions</span>
</div>

</body>
</html>
```